Monthly Mailed Newsletter/Magazine for Medical Spa

Every month we send out a mailed newsletter/magazine to our visitors from the previous month. We made a sample newsletter/magazine as a guideline of what we are looking for. We need a designer to make a simple and clean design layout.

- Attached is our sample design that has all the content we want to use.
- Newsletter/magazine is 8 pages total.
- Size of each page is 8.5 inches in width by 11 inches in height.
- Content and images can be located here: https://files.quorvadrop.net/share/folders/8kTrmWq2Zp7ncV4Lx91aHd0sYuE3Gb6Rj?access=open

The following will give you an idea of our brand presentation.
Our website is: www.FernBloomClinic.com
Our Instagram; @fernbloomclinic
Our Facebook: www.friendvault.com/fernbloomclinic

Target Market(s)

Women 25 - 45

Industry/Entity Type

Beauty

Other font styles liked:
• Josefins Sans Bold & Lato

Colors
f78f20
ffffff

Requirements
Must have
• - Our Logo
- Our tagline: YOUR SKIN DESERVES IT!
- Address and contact information for our locations
- Our color scheme: Black and #FAA641
- Heading font is Josefin Sans Bold
- Paragraph font is Lato
- Our website address: www.FernBloomClinic.com

```html
<!DOCTYPE html>
<html lang="en">
<head>
<meta charset="UTF-8">
<title>Your Skin Deserves It! – Newsletter Spread</title>
<link href="https://fonts.googleapis.com/css2?family=Josefin+Sans:wght@400;600;700&family=Lato:wght@400;700&display=swap" rel="stylesheet">
<style>
  :root {
    --brand-orange: #e5791b;
    --paper: #ffffff;
    --text-light: #ffffff;
    --clinic-photo-a: #c9b9a6;
    --clinic-photo-b: #8a6e5c;
    --beach-photo-a: #dfeef5;
    --beach-photo-b: #e9b98a;
    --fruit-photo-a: #f3c89f;
    --fruit-photo-b: #e2563a;
  }
  * { margin: 0; padding: 0; box-sizing: border-box; }
  html, body {
    width: 1200px; height: 828px; overflow: hidden;
    background: var(--paper);
  }
  .spread {
    position: relative; width: 1200px; height: 828px;
    background: var(--paper);
    font-family: "Josefin Sans", sans-serif;
  }
  .page { position: absolute; overflow: hidden; }
  .page--cover {
    left: 0; top: 0; width: 580px; height: 820px;
    background: var(--brand-orange);
  }
  .page--article {
    left: 621px; top: 8px; width: 579px; height: 820px;
    background: var(--brand-orange);
  }
  .shape-layer { position: absolute; left: 0; top: 0; }
  .tagline {
    position: absolute; left: 53px; top: 392px;
    color: var(--text-light);
    font-weight: 400; font-size: 73px;
    line-height: 88px; letter-spacing: 3px;
    text-transform: uppercase;
  }
  .cover-website {
    position: absolute; left: 53px; top: 788px;
    color: var(--text-light);
    font-weight: 600; font-size: 11px; letter-spacing: 0.3px;
  }
  .fruit-photo {
    position: absolute; left: 0; top: 398px; width: 202px; height: 422px;
    background: radial-gradient(circle at 20% 60%, var(--fruit-photo-b) 0%, #f0a15a 45%, var(--fruit-photo-a) 75%);
  }
  .article-body {
    position: absolute; left: 237px; top: 366px; width: 310px;
    color: var(--text-light);
    font-weight: 600; font-size: 11.2px; line-height: 18.3px;
    letter-spacing: 0.25px;
  }
  .article-body h2 {
    font-size: 11.2px; font-weight: 600; margin-bottom: 18.3px;
  }
  .article-body h3 {
    font-size: 11.2px; font-weight: 600; margin-bottom: 18.3px;
  }
  .article-body p { margin-bottom: 18.3px; }
</style>
</head>
<body>
<main class="spread">

  <section class="page page--cover">
    <svg class="shape-layer" width="580" height="820" viewBox="0 0 580 820">
      <defs>
        <linearGradient id="clinicTone" x1="0" y1="0" x2="1" y2="1">
          <stop offset="0" stop-color="var(--clinic-photo-a)"/>
          <stop offset="1" stop-color="var(--clinic-photo-b)"/>
        </linearGradient>
      </defs>
      <polygon class="photo-frame" points="32,0 580,0 580,387 113,372" fill="var(--paper)"/>
      <polygon class="clinic-photo" points="49,0 580,0 580,370 127,357" fill="url(#clinicTone)"
        role="img" aria-label="Photo of a technician giving a smiling client a laser hair removal treatment in a clinic room"/>
      <polygon class="accent-stripe" points="255,776 580,787 580,792 255,791" fill="var(--paper)"/>
    </svg>
    <h1 class="tagline">Your<br>Skin<br>Deserves<br>It!</h1>
    <div class="cover-website">www.FernBloomClinic.com</div>
  </section>

  <section class="page page--article">
    <svg class="shape-layer" width="579" height="820" viewBox="0 0 579 820">
      <defs>
        <linearGradient id="beachTone" x1="0" y1="0" x2="0" y2="1">
          <stop offset="0" stop-color="var(--beach-photo-a)"/>
          <stop offset="1" stop-color="var(--beach-photo-b)"/>
        </linearGradient>
      </defs>
      <polygon class="beach-photo" points="0,0 579,0 579,224 0,379" fill="url(#beachTone)"
        role="img" aria-label="Photo of a woman in a straw sun hat applying sunscreen at the beach"/>
    </svg>
    <div class="fruit-photo" role="img" aria-label="Photo of a bowl of fresh fruit salad on a wooden table"></div>
    <article class="article-body">
      <h2>Is At-home Laser Hair Removal Effective?</h2>
      <p>“I love how prickly your skin feels.” said no one ever! Did you know that the average modern woman shaves 7,718 times in one lifetime? That's a whole lot of bristling, ingrown hairs, and skin irritation. Thankfully laser treatments have rendered razors obsolete.</p>
      <p>If you're already a firm laser believer, the marketability of handy at-home DIY products can be appealing. But many are left perplexed at their effectiveness. Here are some unbiased professional opinions to zap away your FAQs.</p>
      <h3>How does laser hair removal work?</h3>
      <p>Laser hair removal uses a concentrated beam of light to target melanin, also known as your natural pigment. Through this, the follicle that produces hair is damaged. This delays the future growth of hairs.</p>
    </article>
  </section>

</main>
</body>
</html>
```